Flyer-Design für Einzelhandel/Online-Shop für Werbetechnikzubehör
Zielgruppe
Wir sind ein Einzelhandel / Onlineshop für Werbetechnikzubehör. Plotterfolie, Plotter, DIY-Artikel. Wir kommen mitten aus dem Ruhrgebiet und unser Name verbindet das Plotten und unsere Herkunft. „Falzwerkstück“
Unsere Zielgruppe sind Kreative aus dem Bastel- / Nähbereich.
Aufgabenstellung
Wir legen wert auf die Verbindung zum Ruhrgebiet (Zechen und co.) Anbei stellen wir auch eine Datei zur Verfügung, die bereits auf unserem Auto und Gutscheinen implementiert ist. Gerne darf diese genutzt werden.
Wir legen Wert auf Gradlinigkeit und Übersichtlichkeit.
Unser Flyer soll ein A6 Format sein (Datenformat: 154 x 111 mm
3 mm Beschnitt) diesen wir mit einem Rabattcode versehen wollen.
Des Weiteren benötigen wir auch die Abbidung von Instagram / Facebook / Homepage.
Daher benötigen wir das Design natürlich auch in einem Bearbeitungsmodus für ai.
Gerade die Felder Rabattcode und Gutscheinbedingungen sollten beachtet werden.
10% auf alle Vinyl, Flex & Flockfolie (Bogenware)
Der Flyer wird als Versandbeileger für befreundete Unternehmen benötigt.
Wir möchten mit diesem Flyer Neukunden gewinnen.
Der Flyer kann beidseitig gestaltet werden. Hoch oder Quer ist auch frei wählbar.
Unsere Farben sind als Datei hochgeladen.

```html
<!DOCTYPE html>
<html lang="de">
<head>
<meta charset="utf-8">
<title>Falzwerkstück – Neukundenrabatt Flyer</title>
<link rel="stylesheet" href="https://fonts.googleapis.com/css2?family=Source+Sans+3:wght@400;600;700&display=swap">
<style>
  :root {
    --teal: #4b97a7;
    --graphite: #58585a;
    --ink: #555557;
    --skyline-faint: #e2e2e2;
    --paper: #ffffff;
    --stage: #ffffff;
  }
  * { margin: 0; padding: 0; box-sizing: border-box; }
  html, body {
    width: 1140px; height: 1200px; overflow: hidden;
    background: var(--stage);
    font-family: "Source Sans 3", "Source Sans Pro", Arial, sans-serif;
  }
  .sheet { position: relative; width: 1140px; height: 1200px; }
  .flyer {
    position: absolute; left: 180px; width: 780px; height: 555px;
    background: var(--paper);
    box-shadow: 0 1px 5px rgba(0,0,0,.28);
    overflow: hidden;
  }
  .flyer--front { top: 30px; }
  .flyer--back { top: 615px; }

  /* front side */
  .skyline {
    position: absolute; left: 18px; right: 18px; top: 44px; height: 134px;
    background: linear-gradient(to top, var(--graphite) 30%, #8a8a8c 100%);
    opacity: .85;
  }
  .title-band {
    position: absolute; left: 0; right: 0; top: 176px; height: 68px;
    background: var(--graphite);
    color: #fff; font-weight: 600; font-size: 41px; letter-spacing: .5px;
    text-align: center; line-height: 70px;
  }
  .rule { position: absolute; left: 0; right: 0; }
  .rule--teal { top: 258px; height: 3px; background: var(--teal); }
  .rule--gray { top: 269px; height: 2px; background: var(--graphite); }
  .brand {
    position: absolute; left: 0; right: 0; top: 345px;
    display: flex; flex-direction: column; align-items: center; gap: 22px;
  }
  .brand__mark { width: 34px; height: 34px; background: var(--teal); }
  .brand__name {
    font-size: 46px; font-weight: 400; color: var(--graphite);
    letter-spacing: .5px; line-height: 1;
  }

  /* back side */
  .back-brand {
    position: absolute; left: 49px; top: 108px;
    font-size: 22px; font-weight: 600; color: var(--teal); line-height: 1;
  }
  .skyline--faint {
    position: absolute; left: 408px; width: 317px; top: 30px; height: 94px;
    background: linear-gradient(to top, var(--skyline-faint), #f2f2f2);
  }
  .head-rule {
    position: absolute; left: 232px; right: 48px; top: 123px; height: 3px;
    background: var(--teal);
  }
  .back-title {
    position: absolute; right: 48px; top: 144px;
    font-size: 32px; font-weight: 600; color: var(--graphite); letter-spacing: .5px;
  }
  .field { position: absolute; top: 232px; }
  .field__label {
    font-size: 21px; font-weight: 600; color: var(--teal); line-height: 1;
    padding-bottom: 30px; border-bottom: 2px solid var(--teal);
  }
  .field--date { left: 49px; width: 266px; }
  .field--code { left: 408px; width: 324px; }
  .terms {
    position: absolute; left: 49px; right: 60px; top: 333px;
    font-size: 13.5px; color: var(--ink); line-height: 1.22;
  }
  .terms p + p { margin-top: 12px; }
  .terms strong { color: var(--teal); font-weight: 600; }
  .contact {
    position: absolute; right: 48px; top: 490px;
    display: flex; align-items: center; gap: 12px;
    font-size: 17px; color: var(--teal);
  }
  .contact__web { font-weight: 600; }
  .contact__social { display: flex; gap: 8px; margin-left: 18px; }
  .contact__social span {
    width: 30px; height: 30px; border-radius: 4px; background: var(--graphite);
  }
</style>
</head>
<body>
<main class="sheet">

  <section class="flyer flyer--front" aria-label="Vorderseite">
    <div class="skyline" role="img" aria-label="Silhouette der Ruhrgebiets-Skyline mit Fördertürmen, Tetraeder, Windrad und Fernsehturm"></div>
    <div class="title-band">NEUKUNDENRABATT</div>
    <div class="rule rule--teal"></div>
    <div class="rule rule--gray"></div>
    <div class="brand">
      <span class="brand__mark"></span>
      <span class="brand__name">FALZWERKSTÜCK</span>
    </div>
  </section>

  <section class="flyer flyer--back" aria-label="Rückseite">
    <span class="back-brand">Falzwerkstück</span>
    <div class="skyline--faint" role="img" aria-label="Blasse Silhouette der Ruhrgebiets-Skyline mit Fördertürmen"></div>
    <div class="head-rule"></div>
    <h1 class="back-title">NEUKUNDENRABATT</h1>

    <div class="field field--date"><div class="field__label">DATUM</div></div>
    <div class="field field--code"><div class="field__label">RABATT-CODE</div></div>

    <div class="terms">
      <p><strong>BEDINGUNGEN:</strong> Lorem ipsum dolor sit amet, consectetuer adipiscing elit, sed diam nonummy nibh euismod incidunt ut laoreet dolore magna aliquam erat volutpat.</p>
      <p>Ut wisi enim ad minim veniam, quis nostrud exercitation ullamcorper suscipit lobortis nisl ut aliquip ex ea commodo consequat. Duis autem vel eum iriure dolor in.</p>
    </div>

    <div class="contact">
      <span>Lindenhofstr. 14</span>
      <span>|</span>
      <span>44135 Dortmund</span>
      <span>|</span>
      <span class="contact__web">www.falzwerkstueck.de</span>
      <span class="contact__social" aria-label="Soziale Netzwerke"><span></span><span></span></span>
    </div>
  </section>

</main>
</body>
</html>
```